My Business is Car Dealership, we sale cars and trucks, I’m looking for a sign design
I need 2 signage
9ā€ by 7ā€ feet.
the other sign is 3" feet high and the width is 12" feet

For further reference about the company , you can check my website
www.harrowbayautosale.com

Industry/Entity Type

Business

Requirements
Must have
• picture of 2018 marlo K240 or 2018 Vantrelle Duskmoor
Nice to have
• the business name Harrow Bay Auto Sale visible from far distance

```html
<!DOCTYPE html>
<html lang="en">
<head>
<meta charset="utf-8">
<title>Harrow Bay Auto Sale – Sign</title>
<link rel="stylesheet" href="https://fonts.googleapis.com/css2?family=Roboto:wght@300;700;900&family=Roboto+Condensed:wght@700&display=swap">
<style>
  :root {
    --wall: #d9dadb;
    --sign-black: #050505;
    --brand-red: #e0202a;
    --burst-red: #e2483a;
    --white: #ffffff;
    --car-orange: #e2561c;
    --car-deep: #a8330f;
    --car-shadow: #2a1c14;
    --haze-olive: #4d5420;
    --haze-violet: #3a2350;
  }
  html, body {
    margin: 0;
    width: 1200px;
    height: 1200px;
    overflow: hidden;
    background: var(--wall);
  }
  .sign {
    position: absolute;
    left: 150px;
    top: 21px;
    width: 900px;
    height: 1157px;
    overflow: hidden;
    background: var(--sign-black);
    font-family: "Roboto", sans-serif;
    color: var(--white);
  }
  .sign-backdrop {
    position: absolute;
    inset: 0;
    background:
      radial-gradient(ellipse 55% 40% at 80% 40%, rgba(77,84,32,.55), transparent 70%),
      radial-gradient(ellipse 35% 30% at 15% 55%, rgba(90,80,20,.45), transparent 70%),
      radial-gradient(ellipse 30% 25% at 8% 90%, rgba(58,35,80,.6), transparent 70%),
      radial-gradient(ellipse 40% 25% at 85% 5%, rgba(90,40,40,.4), transparent 70%);
  }
  .brand-mark {
    position: absolute;
    left: 374px;
    top: 70px;
    width: 152px;
    height: 152px;
    box-sizing: border-box;
    border: 6px solid var(--brand-red);
    border-radius: 50%;
  }
  .brand-name {
    position: absolute;
    top: 236px;
    left: 0;
    width: 100%;
    margin: 0;
    text-align: center;
    font-family: "Roboto Condensed", sans-serif;
    font-weight: 700;
    font-size: 52px;
    line-height: 60px;
    letter-spacing: 1px;
    color: var(--brand-red);
  }
  .tagline {
    position: absolute;
    top: 302px;
    left: 0;
    width: 100%;
    margin: 0;
    text-align: center;
    font-weight: 300;
    font-size: 41px;
    line-height: 50px;
  }
  .tagline strong { font-weight: 700; }
  .car-photo {
    position: absolute;
    left: 284px;
    top: 452px;
    width: 616px;
    height: 572px;
    background:
      radial-gradient(ellipse 75% 60% at 62% 52%, var(--car-orange), var(--car-deep) 65%, var(--car-shadow) 100%),
      var(--car-shadow);
  }
  .sale-burst {
    position: absolute;
    left: 44px;
    top: 522px;
    width: 308px;
    height: 308px;
  }
  .sale-burst-text {
    position: absolute;
    left: 44px;
    top: 522px;
    width: 308px;
    height: 308px;
    display: flex;
    flex-direction: column;
    justify-content: center;
    align-items: center;
    font-family: "Roboto Condensed", sans-serif;
    font-weight: 700;
    font-size: 45px;
    line-height: 56px;
    text-align: center;
  }
  .apply-heading {
    position: absolute;
    left: 94px;
    top: 866px;
    margin: 0;
    font-weight: 700;
    font-size: 45px;
  }
  .web-pill {
    position: absolute;
    left: 67px;
    top: 927px;
    width: 773px;
    height: 79px;
    box-sizing: border-box;
    border: 5px solid var(--brand-red);
    border-radius: 40px;
    background: linear-gradient(90deg, rgba(5,5,5,.9), rgba(5,5,5,.35));
    padding-left: 25px;
    display: flex;
    align-items: center;
    font-weight: 700;
    font-size: 36px;
  }
  .phone-number {
    position: absolute;
    left: 0;
    top: 1012px;
    width: 100%;
    text-align: center;
    font-weight: 900;
    font-size: 104px;
    line-height: 120px;
    color: var(--white);
    -webkit-text-stroke: 4px var(--brand-red);
    paint-order: stroke fill;
  }
</style>
</head>
<body>
  <main class="sign">
    <div class="sign-backdrop"></div>

    <div class="brand-mark" aria-hidden="true"></div>
    <h1 class="brand-name">Harrow Bay Auto Sale</h1>

    <p class="tagline">
      To Provide a <strong>Fair</strong>, <strong>Respectful</strong>,<br>
      and <strong>Efficient Service</strong> to all Customers,<br>
      <strong>Everytime, All the Time</strong>
    </p>

    <div class="car-photo" role="img" aria-label="Photo of a glossy orange sports sedan, front three-quarter view with headlights and grille"></div>

    <svg class="sale-burst" viewBox="0 0 308 308" aria-hidden="true">
      <g fill="var(--burst-red)">
        <rect x="48" y="48" width="212" height="212" transform="rotate(0 154 154)"/>
        <rect x="48" y="48" width="212" height="212" transform="rotate(15 154 154)"/>
        <rect x="48" y="48" width="212" height="212" transform="rotate(30 154 154)"/>
        <rect x="48" y="48" width="212" height="212" transform="rotate(45 154 154)"/>
        <rect x="48" y="48" width="212" height="212" transform="rotate(60 154 154)"/>
        <rect x="48" y="48" width="212" height="212" transform="rotate(75 154 154)"/>
      </g>
    </svg>
    <div class="sale-burst-text">
      <span>WE SALE</span>
      <span>CARS &amp;</span>
      <span>TRUCKS</span>
    </div>

    <h2 class="apply-heading">APPLY ONLINE</h2>
    <div class="web-pill">www.harrowbayautosale.com</div>

    <div class="phone-number">555-307-4190</div>
  </main>
</body>
</html>
```